Silver Kettle Consulting

I need a business card design and for my consulting business. I provide outsourced CFO services for start-ups and high growth companies. I call my company Silver Kettle because building a company is similar to building a stone pathway, selecting each stone and planning several stones head in order to properly place them - all while keeping an eye on the final design and curve of the path. The underlying idea I want to express with my marketing images is that I'm someone that you can count on to help build your business and be there step by step to help. I'm not the old gray-haired CFO that many folks think of. :) I've included a one-page summery that I'm working on, it includes a summary of what I do. I've used a muted pathway and with greens in the header , and do like the green, but am open to other colors if they work well. Would like something that looks like a pathway, but a more abstract version instead of a picture.

Marketing

```html
<!DOCTYPE html>
<html lang="en">
<head>
<meta charset="utf-8">
<title>Silver Kettle Consulting – Business Card</title>
<link rel="stylesheet" href="https://fonts.googleapis.com/css2?family=Ubuntu:wght@400&display=swap">
<style>
  :root {
    --page-bg: #d9d9d7;
    --card-green: #0f8f57;
    --accent-red: #a3122a;
    --accent-gold: #e3dc8c;
    --ink-dark: #111814;
    --ink-light: #e9efe9;
    --card-shadow: 0 6px 18px rgba(0, 0, 0, 0.22);
  }
  * { box-sizing: border-box; margin: 0; padding: 0; }
  html, body {
    width: 1200px;
    height: 1000px;
    overflow: hidden;
    background: var(--page-bg);
    font-family: "Ubuntu", sans-serif;
  }
  .canvas {
    position: relative;
    width: 1200px;
    height: 1000px;
  }
  .card {
    position: absolute;
    left: 210px;
    width: 780px;
    height: 446px;
    background: var(--card-green);
    box-shadow: var(--card-shadow);
    overflow: hidden;
  }
  .card--brand { top: 36px; }
  .card--contact { top: 518px; }

  /* Brand side */
  .brand-block {
    position: absolute;
    right: 56px;
    top: 62px;
    text-align: right;
    color: var(--ink-dark);
  }
  .brand-name {
    font-size: 62px;
    font-weight: 400;
    letter-spacing: 2px;
    line-height: 1;
  }
  .brand-sub {
    margin-top: 12px;
    font-size: 27px;
    line-height: 1;
  }
  .brand-rule {
    position: absolute;
    left: 0;
    right: 0;
    top: 212px;
    height: 6px;
    background: var(--accent-red);
  }
  .brand-tagline {
    position: absolute;
    right: 40px;
    top: 240px;
    width: 640px;
    text-align: center;
    font-size: 22px;
    line-height: 1.3;
    color: var(--ink-dark);
  }

  /* Contact side */
  .person {
    position: absolute;
    left: 58px;
    top: 58px;
    color: var(--ink-light);
  }
  .person-name {
    font-size: 32px;
    line-height: 1.2;
  }
  .person-role {
    margin-top: 14px;
    font-size: 28px;
    line-height: 1.2;
  }
  .mini-brand {
    position: absolute;
    right: 50px;
    top: 58px;
    text-align: right;
    color: var(--ink-light);
  }
  .mini-brand-name {
    font-size: 27px;
    letter-spacing: 1px;
    line-height: 1;
  }
  .mini-brand-sub {
    margin-top: 8px;
    font-size: 15px;
    line-height: 1;
  }
  .path-motif {
    position: absolute;
    left: 340px;
    top: 150px;
    width: 90px;
    height: 170px;
    border-radius: 4px;
    background: linear-gradient(160deg, rgba(163, 18, 42, 0.55), rgba(227, 220, 140, 0.45));
  }
  .contact-list {
    position: absolute;
    left: 340px;
    top: 335px;
    list-style: none;
    color: var(--ink-light);
  }
  .contact-item {
    display: flex;
    align-items: center;
    gap: 22px;
    font-size: 28px;
    height: 46px;
  }
  .contact-icon {
    width: 38px;
    height: 40px;
    flex: none;
  }
</style>
</head>
<body>
<main class="canvas">

  <section class="card card--brand" aria-label="Card front">
    <div class="brand-block">
      <div class="brand-name">Silver Kettle</div>
      <div class="brand-sub">Consulting Services</div>
    </div>
    <div class="brand-rule"></div>
    <p class="brand-tagline">Exclusive Finance and Operations Expertise on a Part-time, Ongoing Engagement or Project Basis</p>
  </section>

  <section class="card card--contact" aria-label="Card back">
    <div class="person">
      <div class="person-name">Dana Whitfield, CPA</div>
      <div class="person-role">Consultant</div>
    </div>

    <div class="mini-brand">
      <div class="mini-brand-name">Silver Kettle</div>
      <div class="mini-brand-sub">Consulting Services</div>
    </div>

    <div class="path-motif" role="img" aria-label="Abstract pathway motif in red and gold"></div>

    <ul class="contact-list">
      <li class="contact-item">
        <svg class="contact-icon" viewBox="0 0 38 40" aria-hidden="true">
          <rect x="9" y="2" width="20" height="36" rx="3" fill="none" stroke="var(--accent-gold)" stroke-width="3"/>
          <line x1="16" y1="33" x2="22" y2="33" stroke="var(--accent-gold)" stroke-width="2"/>
        </svg>
        <span>217-555-0142</span>
      </li>
      <li class="contact-item">
        <svg class="contact-icon" viewBox="0 0 38 40" aria-hidden="true">
          <rect x="2" y="9" width="34" height="22" fill="var(--accent-gold)"/>
          <polyline points="2,9 19,23 36,9" fill="none" stroke="var(--card-green)" stroke-width="2"/>
          <line x1="2" y1="31" x2="14" y2="19" stroke="var(--card-green)" stroke-width="2"/>
          <line x1="36" y1="31" x2="24" y2="19" stroke="var(--card-green)" stroke-width="2"/>
        </svg>
        <span>dana@silverkettle.com</span>
      </li>
    </ul>
  </section>

</main>
</body>
</html>
```